Web page design for podiatry office*

Need a web page for our podiatry office. It should feature most of our services, hours, directions and location. Should include a short bio of the doctor and a contact page.

Coding

Coded - Design and coding required

Number of Pages Required

1 page

Colors

Designer to choose colors to be used in the design.

```html
<!DOCTYPE html>
<html lang="en">
<head>
<meta charset="utf-8">
<title>Podiatry Office</title>
<link href="https://fonts.googleapis.com/css2?family=Ubuntu:wght@300;400;500&family=Poppins:wght@600&family=Hind:wght@400;500&family=Roboto+Condensed:wght@400&display=swap" rel="stylesheet">
<style>
:root{
  --orange:#f4623a;
  --orange-soft:#f7b3a0;
  --ink:#222;
  --text:#666;
  --white:#fff;
  --dark:#2b2b2b;
}
*{margin:0;padding:0;box-sizing:border-box}
html,body{width:1200px;height:2625px;overflow:hidden;background:var(--white)}
body{position:relative;font-family:'Hind',sans-serif;color:var(--ink)}
.abs{position:absolute}
.header{left:0;top:0;width:1200px;height:83px;background:rgba(255,255,255,.96);z-index:5;box-shadow:0 1px 4px rgba(0,0,0,.05)}
.brand{font-family:'Ubuntu',sans-serif;font-weight:500;font-size:29px;letter-spacing:.2px}
.brand .accent{color:var(--orange)}
.header .brand{left:76px;top:24px;color:#333}
.nav{left:594px;top:32px;display:flex;gap:26px;font-family:'Ubuntu',sans-serif;font-size:16px;color:#333}
.nav .active{color:var(--orange)}
.phone{left:943px;top:20px;display:flex;align-items:center;gap:10px;color:var(--orange);font-family:'Ubuntu',sans-serif;font-weight:500;font-size:21px}
.phone-ring{width:42px;height:42px;border:1.5px solid var(--orange);border-radius:50%;display:flex;align-items:center;justify-content:center}
.hero{left:0;top:0;width:1200px;height:677px;background:#fff;overflow:hidden}
.hero-photo{left:430px;top:0;width:770px;height:677px;background:linear-gradient(120deg,#fff 0%,#f6ece6 35%,#efd9cf 70%,#f4e7e0 100%)}
.hero-shapes{left:0;top:0}
.hero-kicker{left:82px;top:243px;font-family:'Ubuntu',sans-serif;font-weight:300;font-size:40px;color:#333}
.hero-title{left:78px;top:288px;font-family:'Poppins',sans-serif;font-weight:600;font-size:64px;color:#111;letter-spacing:-.5px}
.hero-text{left:79px;top:374px;width:400px;font-family:'Roboto Condensed',sans-serif;font-size:18px;line-height:27px;color:#222}
.btn{background:var(--orange);color:var(--white);font-family:'Ubuntu',sans-serif;font-size:19px;display:flex;align-items:center;justify-content:center}
.hero .btn{left:78px;top:445px;width:172px;height:56px}
.dots{left:1155px;top:295px;display:flex;flex-direction:column;gap:10px}
.dots span{width:14px;height:14px;border:1.5px solid var(--orange);border-radius:50%;background:#fff}
.dots .on{background:var(--orange)}
.services{left:0;top:677px;width:1200px;height:515px;background:var(--orange)}
.section-title{font-family:'Ubuntu',sans-serif;font-weight:500;font-size:44px;color:var(--white);text-align:center;width:1200px;left:0}
.services .section-title{top:62px}
.card{top:141px;width:323px;height:312px;background:var(--white)}
.card-photo{width:323px;height:250px}
.card-label{height:62px;display:flex;align-items:center;justify-content:space-between;padding:0 22px;font-family:'Ubuntu',sans-serif;font-size:15.5px;color:#222}
.bio{left:0;top:1192px;width:1200px;height:523px}
.bio-photo{left:140px;top:53px;width:395px;height:470px;background:radial-gradient(ellipse at 50% 60%,#eef0f2 0%,#dfe3e7 55%,#fff 100%)}
.bio-title{left:621px;top:58px;font-family:'Ubuntu',sans-serif;font-weight:500;font-size:44px;color:#222}
.bio-text{left:625px;width:410px;font-size:14px;line-height:27px;color:var(--text)}
.bio .btn{left:626px;top:405px;width:172px;height:56px}
.cta{left:0;top:1715px;width:1200px;height:520px;background:radial-gradient(ellipse at 47% 68%,#7a3430 0%,#3a3332 30%,#262626 75%)}
.cta-kicker{top:140px;left:0;width:1200px;text-align:center;color:#eee;font-size:17px}
.cta .section-title{top:172px;font-size:46px}
.cta .btn{left:457px;top:239px;width:286px;height:56px}
.footer{left:0;top:2235px;width:1200px;height:390px;background:var(--orange)}
.info{left:183px;top:2125px;width:834px;height:219px;background:var(--white);display:flex;padding:37px 0 0 28px;z-index:3}
.info-col{width:271px;padding:0 25px 0 0;border-right:1px solid #e6e6e6;height:150px}
.info-col:last-child{border:none}
.info-col+.info-col{padding-left:25px}
.info-head{display:flex;align-items:center;gap:14px;font-family:'Ubuntu',sans-serif;font-weight:500;font-size:21px;color:#222;margin-bottom:16px}
.info-body{padding-left:44px;font-size:14px;line-height:31px;color:var(--text)}
.info-body em{font-style:normal;color:var(--orange)}
.footer .brand{left:0;width:1200px;text-align:center;top:158px;color:var(--white)}
.footer .brand .accent{color:#fff;opacity:1}
.social{left:527px;top:212px;display:flex;gap:8px}
.social span{width:41px;height:41px;border-radius:50%;background:var(--white)}
.foot-links{left:0;width:1200px;top:282px;text-align:center;color:#fff;font-size:15px}
.copy{left:0;width:1200px;top:309px;text-align:center;color:#fff;font-size:13.5px}
</style>
</head>
<body>
<section class="hero abs">
  <div class="hero-photo abs" role="img" aria-label="Close-up photograph of bare feet stepping forward"></div>
  <svg class="hero-shapes abs" width="1200" height="677" viewBox="0 0 1200 677">
    <polygon points="140,664 425,404 718,664" fill="#f7b3a0" opacity=".55"/>
    <polygon points="252,677 527,402 802,677" fill="#f4623a" opacity=".5"/>
  </svg>
  <div class="hero-kicker abs">Your Next</div>
  <div class="hero-title abs">Step Forward</div>
  <p class="hero-text abs">Lorem Ipsum is simply dummy text of the printing and typesetting industry&nbsp; Lorem Ipsum has been</p>
  <div class="btn abs">CONTACT US</div>
  <div class="dots abs"><span></span><span></span><span></span><span class="on"></span><span></span></div>
</section>

<header class="header abs">
  <div class="brand abs"><span class="accent">PODIATRY</span> OFFICE</div>
  <nav class="nav abs"><span class="active">HOME</span><span>BIO</span><span>SERVICES</span><span>CONTACT US</span></nav>
  <div class="phone abs">
    <span class="phone-ring"><svg width="22" height="22" viewBox="0 0 24 24" fill="none" stroke="#f4623a" stroke-width="1.8"><path d="M5 3h4l2 5-2.5 1.5a11 11 0 0 0 6 6L16 13l5 2v4a2 2 0 0 1-2 2A16 16 0 0 1 3 5a2 2 0 0 1 2-2z"/></svg></span>
    <span>123 456 7890</span>
  </div>
</header>

<section class="services abs">
  <h2 class="section-title abs">OUR BEST SERVICES</h2>
  <div class="card abs" style="left:94px">
    <div class="card-photo" role="img" aria-label="Photograph of a podiatrist treating a patient's foot" style="background:linear-gradient(135deg,#eee9e4,#e8c9b5 60%,#cfe3ee)"></div>
    <div class="card-label">GENERAL TREATMENT<svg width="26" height="26" viewBox="0 0 26 26"><circle cx="13" cy="13" r="11" fill="none" stroke="#f4623a" stroke-width="2.5"/><path d="M7 13h11M13 8l5 5-5 5" fill="none" stroke="#f4623a" stroke-width="2.5"/></svg></div>
  </div>
  <div class="card abs" style="left:438px">
    <div class="card-photo" role="img" aria-label="Photograph of hands stretching a bare foot" style="background:linear-gradient(135deg,#f0eeee,#e9cfbf 55%,#e2e1e1)"></div>
    <div class="card-label">SPECIALISED&nbsp; TREATMENT<svg width="26" height="26" viewBox="0 0 26 26"><circle cx="13" cy="13" r="11" fill="none" stroke="#f4623a" stroke-width="2.5"/><path d="M7 13h11M13 8l5 5-5 5" fill="none" stroke="#f4623a" stroke-width="2.5"/></svg></div>
  </div>
  <div class="card abs" style="left:782px">
    <div class="card-photo" role="img" aria-label="Photograph of a runner's foot with highlighted bones" style="background:linear-gradient(160deg,#d9dcdf,#e6a58c 45%,#555a60)"></div>
    <div class="card-label">SPORTS INJURY<svg width="26" height="26" viewBox="0 0 26 26"><circle cx="13" cy="13" r="11" fill="none" stroke="#f4623a" stroke-width="2.5"/><path d="M7 13h11M13 8l5 5-5 5" fill="none" stroke="#f4623a" stroke-width="2.5"/></svg></div>
  </div>
</section>

<section class="bio abs">
  <div class="bio-photo abs" role="img" aria-label="Portrait of the podiatrist in a white coat holding a clipboard"></div>
  <h2 class="bio-title abs">BIO</h2>
  <p class="bio-text abs" style="top:130px">Lorem Ipsum is simply dummy text of the printing and typesetting industry. Lorem Ipsum has been the industry's standard dummy text ever since the 1500s</p>
  <p class="bio-text abs" style="top:226px">Lorem Ipsum is simply dummy text of the printing and the typesetting industry. Lorem Ipsum has been the industry's standard dummy text ever since the 1500s, when an unkno printer took a galley of type and scrambled it to make a type specimen book. It has survived not only five centuries, but is the leap into electronic typesetting, remaining.</p>
  <div class="btn abs">LEARN MORE</div>
</section>

<section class="cta abs" role="img" aria-label="Dark photograph of a runner holding a sore ankle">
  <div class="cta-kicker abs">Setting the Standards for</div>
  <h2 class="section-title abs">QUALITY PATIENT CARE</h2>
  <div class="btn abs">BOOK AN APPOINTMENT</div>
</section>

<footer class="footer abs">
  <div class="brand abs"><span class="accent">PODIATRY</span> OFFICE</div>
  <div class="social abs"><span></span><span></span><span></span></div>
  <div class="foot-links abs">Home | Bio | &nbsp;Services | Contact</div>
  <div class="copy abs">©PODIATRY OFFICE - 2019 All Rights Reserved.</div>
</footer>

<section class="info abs">
  <div class="info-col">
    <div class="info-head"><svg width="30" height="30" viewBox="0 0 30 30"><circle cx="15" cy="15" r="12" fill="none" stroke="#f4623a" stroke-width="2.5"/><path d="M15 8v7h6" fill="none" stroke="#f4623a" stroke-width="2.5"/></svg>HOURS</div>
    <div class="info-body">Mon-Fri : 9am to 5pm<br>Saturday : 9am to 3pm<br>Sunday : <em>Closed</em></div>
  </div>
  <div class="info-col">
    <div class="info-head"><svg width="30" height="30" viewBox="0 0 30 30" fill="#f4623a"><rect x="13.5" y="3" width="3" height="25"/><path d="M4 7h20l3 3-3 3H4z"/><path d="M26 15H6l-3 3 3 3h20z"/></svg>DIRECTIONS</div>
    <div class="info-body">101 - Lorem ipsum the simple text of print type setting industry.</div>
  </div>
  <div class="info-col">
    <div class="info-head"><svg width="30" height="30" viewBox="0 0 30 30"><path d="M15 28s9-9 9-16a9 9 0 0 0-18 0c0 7 9 16 9 16z" fill="none" stroke="#f4623a" stroke-width="2.5"/><circle cx="15" cy="12" r="3.5" fill="#f4623a"/></svg>LOCATION</div>
    <div class="info-body">101 - Lorem ipsum the simple text of print type setting industry.</div>
  </div>
</section>
</body>
</html>
```